Laser Tattoo Removal Business Cards

We are looking for a professional business card design for a laser tattoo removal business. Ideally looking for a black business card design. The name of the business is Lumen Ink Clearing. We place our cards at local tattoo shops so we ideally are looking for something trendy/edgy to draw both male and female clientele in.

Target Market(s)

Male/Female ages 18-60

Contact Information for Business Card

black background ideally.. hoping to stay within greys, whites and black

Font styles to use
Serif
Sans Serif

Colors
121212
a9a9a9
5c5c5c
f5f5f5
ffffff
7f7f7f
606060
848484
9d9d9d

Requirements
Must have
• Employee Info:
• Marisol Dunmore
• Chief Executive Offer
• m: 555.014.3210
• w: 555.017.8640
• f: 555.019.2475
• mdunmore@lumeninkclearing.com
• Address:
• 4185 Fenwick Pkwy, Suite 210
• Alder Point, NC 28950
• Website:
• www.lumeninkclearing.com
Nice to have
• Myabe business name on back or logo on back and employee info on the front

```html
<!DOCTYPE html>
<html lang="en">
<head>
<meta charset="utf-8">
<title>Lumen Ink Clearing – Business Cards</title>
<link href="https://fonts.googleapis.com/css2?family=Josefin+Sans:wght@400&family=Montserrat:wght@700&family=Open+Sans:wght@400&family=Pinyon+Script&display=swap" rel="stylesheet">
<style>
  :root {
    --canvas: #2b2d31;
    --card-dark: #121212;
    --card-light: #ffffff;
    --ink-white: #f5f5f5;
    --ink-grey: #a9a9a9;
    --ink-black: #121212;
    --rule: #5c5c5c;
  }
  * { box-sizing: border-box; margin: 0; padding: 0; }
  html, body {
    width: 1200px;
    height: 900px;
    overflow: hidden;
    background: var(--canvas);
  }
  .stage {
    position: relative;
    width: 1200px;
    height: 900px;
  }
  .card {
    position: absolute;
    top: 301px;
    width: 520px;
    height: 298px;
    border-radius: 3px;
  }
  .card--contact {
    left: 60px;
    background: var(--card-dark);
    color: var(--ink-white);
    text-align: center;
  }
  .card--brand {
    left: 620px;
    background: var(--card-light);
    color: var(--ink-black);
    display: flex;
    flex-direction: column;
    align-items: center;
    justify-content: center;
  }
  .person-name {
    margin-top: 58px;
    font-family: "Montserrat", sans-serif;
    font-weight: 700;
    font-size: 30px;
    letter-spacing: 0.5px;
    text-transform: uppercase;
  }
  .person-title {
    margin-top: 2px;
    font-family: "Pinyon Script", cursive;
    font-size: 27px;
    color: var(--ink-grey);
  }
  .contact-list {
    position: absolute;
    left: 0;
    right: 0;
    bottom: 40px;
    list-style: none;
    font-family: "Open Sans", sans-serif;
    font-size: 12.5px;
    line-height: 1.7;
    color: var(--ink-white);
  }
  .brand-name {
    font-family: "Josefin Sans", sans-serif;
    font-weight: 400;
    color: var(--ink-black);
    text-transform: uppercase;
    text-align: center;
    line-height: 1.1;
  }
  .brand-name__main {
    display: block;
    font-size: 76px;
    letter-spacing: 4px;
  }
  .brand-name__sub {
    display: flex;
    align-items: center;
    justify-content: center;
    gap: 14px;
    margin-top: 14px;
    font-size: 24px;
    letter-spacing: 7px;
  }
  .brand-name__rule {
    display: block;
    width: 34px;
    height: 1px;
    background: var(--rule);
  }
</style>
</head>
<body>
  <main class="stage">
    <section class="card card--contact">
      <h1 class="person-name">Marisol Dunmore</h1>
      <p class="person-title">Chief Executive Officer</p>
      <ul class="contact-list">
        <li>M: 555.014.3210 | W: 555.017.8640 | F: 555.019.2475</li>
        <li>mdunmore@lumeninkclearing.com | www.lumeninkclearing.com</li>
        <li>4185 Fenwick Pkwy, Suite 210, Alder Point, NC 28950</li>
      </ul>
    </section>
    <section class="card card--brand">
      <h2 class="brand-name">
        <span class="brand-name__main">Lumen</span>
        <span class="brand-name__sub">
          <span class="brand-name__rule"></span>
          <span>Ink Clearing</span>
          <span class="brand-name__rule"></span>
        </span>
      </h2>
    </section>
  </main>
</body>
</html>
```